Quillon Maison Wood Fired Pizza business card design

I have a logo and need an eye catching design that will get me noticed.
My business is wood fired pizza. I want a bold design that will make our customers remember us and the food that we serve. Work with the colors of our logo and texts. Maybe add designs that lend to what or how pizza is made using our wood fired oven?

Target Market(s)

Foodies!

Contact Information for Business Card

Quillon Maison Wood Fired Pizza
Our slogan is Fast. Fresh. Handcrafted
Catering for all events

Requirements
Must have
• Dana Porrick
Telephone 570 555 0183
website www.getquillon.example
Facebook @getquillonpizza maybe use the facebook logo next to it
Instagram getquillonpizza maybe use the instagram logo next to it
Catering for all events
Nice to have
• Maybe pizza peels, pizza cutters? Wood? Fired wood? Using our flame in the background?
Please work with different colored text so each sentence stands out? A themed color for facebook?
Maybe work with the colors within our logo?
Please try to use the our quillon font, but not a must have.

```html
<!DOCTYPE html>
<html lang="en">
<head>
<meta charset="utf-8">
<title>Quillon Maison Wood Fired Pizza – Business Card</title>
<link href="https://fonts.googleapis.com/css2?family=Oswald:wght@400;500;600;700&family=Roboto:wght@400;700&family=Alfa+Slab+One&display=swap" rel="stylesheet">
<style>
  :root {
    --page: #ffffff;
    --card-dark: #1c1c1c;
    --card-dark-2: #2b2b2b;
    --card-cream: #f7ece1;
    --cream: #f3e6d3;
    --flame-red: #c8201c;
    --orange: #f0932a;
    --ink: #262626;
    --slogan-fill: #fbe9d0;
    --slogan-stroke: #f2b56b;
  }
  * { margin: 0; padding: 0; box-sizing: border-box; }
  html, body { width: 1200px; height: 1200px; overflow: hidden; background: var(--page); }
  .canvas { position: relative; width: 1200px; height: 1200px; font-family: "Oswald", sans-serif; }

  .card { position: absolute; width: 356px; height: 641px; overflow: hidden; text-align: center; }

  /* Brand lockup: name in one colour, one weight, plus one plain circle */
  .brand-mark { position: absolute; left: 50%; border-radius: 50%; background: var(--flame-red); transform: translateX(-50%); }
  .brand-name { position: absolute; left: 0; right: 0; font-weight: 700; text-transform: uppercase; line-height: 1; }
  .brand-name .brand-line { display: block; }

  /* Front */
  .card-front {
    left: 132px; top: 195px;
    background: linear-gradient(160deg, var(--card-dark-2), var(--card-dark) 70%);
    color: var(--cream);
  }
  .card-front .brand-mark { top: 120px; width: 130px; height: 130px; }
  .card-front .brand-name { top: 440px; color: var(--cream); }
  .card-front .brand-name { top: 288px; }
  .card-front .brand-line.small { font-size: 13px; letter-spacing: 1.5px; margin-bottom: 6px; }
  .card-front .brand-line.large { font-size: 38px; letter-spacing: 3px; }
  .front-established {
    position: absolute; left: 0; right: 0; top: 348px;
    font-size: 8px; letter-spacing: 2px; color: var(--cream);
  }
  .front-slogan {
    position: absolute; left: 0; right: 0; top: 368px;
    font-size: 15px; letter-spacing: 1.2px; color: var(--orange); text-transform: uppercase;
  }
  .front-photo {
    position: absolute; left: 0; right: 0; bottom: 0; height: 225px;
    background:
      radial-gradient(ellipse 30% 38% at 55% 40%, #d99a55 0%, #b5552d 55%, transparent 100%),
      radial-gradient(ellipse 26% 40% at 25% 72%, #d9a060 0%, #a94a28 55%, transparent 100%),
      radial-gradient(ellipse 24% 36% at 58% 82%, #d7a066 0%, #9e4426 55%, transparent 100%),
      radial-gradient(ellipse 60% 50% at 45% 65%, #3b3a2c 0%, transparent 100%);
  }

  /* Back */
  .card-back {
    left: 640px; top: 195px;
    background: var(--card-cream);
    color: var(--ink);
  }
  .card-back .brand-mark { top: 48px; width: 80px; height: 80px; }
  .card-back .brand-name { top: 142px; color: var(--ink); }
  .card-back .brand-line.small { font-size: 10px; letter-spacing: 1.2px; margin-bottom: 5px; }
  .card-back .brand-line.large { font-size: 28px; letter-spacing: 2.5px; }
  .back-established {
    position: absolute; left: 0; right: 0; top: 192px;
    font-size: 7px; letter-spacing: 2px; color: var(--ink);
  }
  .back-name {
    position: absolute; left: 0; right: 0; top: 238px;
    font-weight: 500; font-size: 32px; line-height: 1.15; letter-spacing: 2px;
    text-transform: uppercase; color: var(--orange);
  }
  .contact-list {
    position: absolute; left: 98px; top: 388px;
    list-style: none; text-align: left;
    font-family: "Roboto", sans-serif; font-size: 14px; line-height: 25px; color: var(--ink);
  }
  .contact-phone { padding-left: 14px; }
  .contact-phone strong, .contact-web { font-weight: 700; }
  .contact-social { display: flex; align-items: center; gap: 8px; }
  .contact-social .icon-dot {
    width: 14px; height: 14px; border-radius: 50%; background: var(--ink); flex: none;
  }
  .back-catering {
    position: absolute; left: 0; right: 0; bottom: 52px;
    font-size: 14px; letter-spacing: 1.5px; text-transform: uppercase; color: var(--ink);
  }

  /* Slogan */
  .slogan {
    position: absolute; left: 105px; top: 995px;
    font-family: "Alfa Slab One", serif; font-size: 56px; line-height: 1.2;
    color: var(--slogan-fill);
    -webkit-text-stroke: 1.5px var(--slogan-stroke);
  }
</style>
</head>
<body>
<main class="canvas">

  <section class="card card-front">
    <span class="brand-mark"></span>
    <div class="brand-name">
      <span class="brand-line small">Maison Wood Fired Pizza</span>
      <span class="brand-line large">Quillon</span>
    </div>
    <div class="front-established">EST. 2020</div>
    <p class="front-slogan">Fast. Fresh. Handcrafted</p>
    <div class="front-photo" role="img" aria-label="Photo of wood fired pizza slices with basil on a dark surface"></div>
  </section>

  <section class="card card-back">
    <span class="brand-mark"></span>
    <div class="brand-name">
      <span class="brand-line small">Maison Wood Fired Pizza</span>
      <span class="brand-line large">Quillon</span>
    </div>
    <div class="back-established">EST. 2020</div>
    <h1 class="back-name">Dana &amp; Tessa<br>Porrick</h1>
    <ul class="contact-list">
      <li class="contact-phone">Phone: <strong>570 555 0183</strong></li>
      <li class="contact-social"><span class="icon-dot"></span>@getquillonpizza</li>
      <li class="contact-social"><span class="icon-dot"></span>getquillonpizza</li>
      <li class="contact-web">www.getquillon.example</li>
    </ul>
    <p class="back-catering">Catering for all events</p>
  </section>

  <p class="slogan">Fast. Fresh.<br>Handcrafted.</p>

</main>
</body>
</html>
```